Copperfield Roofing Co. business card design

I am a Roofing contractor in Texas. The name of my company is Copperfield Roofing Co. I also offer a few other services (Christmas light installation, gutters, fencing, pressure washing). However my main gig is roofing. Storm restoration and knowledge of the insurance claim process is my specialty.

My colors are black, red and white. I’d like something pretty simple and clean. Modern looking but with a splash of this red tartan pattern.

I have another version of my logo being edited at the moment where the little top part of the F in roofing that’s currently tartan will be changed to just solid red to make it more visible. So if that’s something you can change in your mock up great. But I can provide the full version once the contest is complete

Target Market(s)

Homeowners

Industry/Entity Type

Roofing

Contact Information for Business Card

Derek Pruitt. 682-555-0193. www.copperfield roofing.co Derek@copperfieldroofing.co

Colors
EB3D1F
EC4F4E
F09395
F8D3D4
FCEDEE

Requirements
Nice to have
• Maybe instead of a business address. I could say serving all DFW Texas or something like that. And maybe add a line somewhere saying deductible assistance? Just a thought

```html
<!DOCTYPE html>
<html lang="en">
<head>
<meta charset="utf-8">
<title>Copperfield Roofing Co. – Business Card</title>
<link href="https://fonts.googleapis.com/css2?family=Montserrat:wght@400;500;700;800&display=swap" rel="stylesheet">
<style>
  :root{
    --red:#d0111b;
    --red-bright:#eb3d1f;
    --black:#050505;
    --white:#ffffff;
    --ink:#1c1c1c;
    --muted:#555555;
    --stage:#3b3b3b;
  }
  *{box-sizing:border-box;margin:0;padding:0}
  html,body{width:1200px;height:1200px;overflow:hidden}
  body{
    background:var(--stage);
    font-family:"Montserrat",sans-serif;
    display:flex;flex-direction:column;align-items:center;justify-content:center;gap:52px;
  }
  .card{
    position:relative;width:880px;height:503px;border-radius:34px;overflow:hidden;
  }
  .card-front{background:var(--white)}
  .card-back{background:var(--black)}

  .bottom-bands{position:absolute;left:0;bottom:0;width:100%;height:80px}

  .contact{position:absolute;left:92px;top:132px}
  .name-block{border-left:7px solid var(--red);padding-left:14px;margin-bottom:34px}
  .name{color:var(--red);font-weight:700;font-size:38px;letter-spacing:1px;line-height:1}
  .role{color:var(--muted);font-weight:500;font-size:15px;letter-spacing:.5px;margin-top:4px}
  .contact-list{list-style:none;display:flex;flex-direction:column;gap:16px;padding-left:40px}
  .contact-item{display:flex;align-items:center;gap:16px;color:var(--ink);font-size:21px;font-weight:400}
  .contact-icon{width:24px;height:24px;flex:none}

  .brand{position:absolute;display:flex;flex-direction:column;align-items:center;text-align:center}
  .card-front .brand{right:70px;top:70px;width:330px}
  .card-back .brand{left:50%;top:50%;transform:translate(-50%,-50%);width:520px}
  .brand-mark{border-radius:50%;background:var(--red)}
  .card-front .brand-mark{width:130px;height:130px;margin-bottom:22px}
  .card-back .brand-mark{width:190px;height:190px;margin-bottom:30px;border:6px solid var(--white)}
  .brand-name{font-weight:800;text-transform:uppercase;line-height:1.05;letter-spacing:1px}
  .card-front .brand-name{color:var(--red);font-size:38px}
  .card-back .brand-name{color:var(--white);font-size:54px}
</style>
</head>
<body>

  <section class="card card-front" aria-label="Business card front">
    <div class="contact">
      <div class="name-block">
        <p class="name">DEREK PRUITT</p>
        <p class="role">OWNER</p>
      </div>
      <ul class="contact-list">
        <li class="contact-item">
          <svg class="contact-icon" viewBox="0 0 24 24" aria-hidden="true"><path fill="#d0111b" d="M6.6 10.8a15 15 0 0 0 6.6 6.6l2.2-2.2c.3-.3.7-.4 1-.2 1.1.4 2.3.6 3.6.6.6 0 1 .4 1 1V20c0 .6-.4 1-1 1A17 17 0 0 1 3 4c0-.6.4-1 1-1h3.5c.6 0 1 .4 1 1 0 1.3.2 2.5.6 3.6.1.3 0 .7-.2 1z"/></svg>
          <span>682-555-0193</span>
        </li>
        <li class="contact-item">
          <svg class="contact-icon" viewBox="0 0 24 24" aria-hidden="true"><rect x="2" y="5" width="20" height="14" rx="1" fill="#d0111b"/><path d="M2.5 6l9.5 7 9.5-7M2.5 18.5l7-6M21.5 18.5l-7-6" stroke="#fff" stroke-width="1.6" fill="none"/></svg>
          <span>Derek@copperfieldroofing.co</span>
        </li>
        <li class="contact-item">
          <svg class="contact-icon" viewBox="0 0 24 24" aria-hidden="true"><circle cx="12" cy="12" r="11" fill="#d0111b"/><g stroke="#fff" stroke-width="1.4" fill="none"><circle cx="12" cy="12" r="8.5"/><ellipse cx="12" cy="12" rx="3.8" ry="8.5"/><path d="M3.5 12h17M5 7.5h14M5 16.5h14"/></g></svg>
          <span>www.copperfieldroofing.co</span>
        </li>
      </ul>
    </div>

    <div class="brand">
      <div class="brand-mark" aria-hidden="true"></div>
      <p class="brand-name">Copperfield<br>Roofing Co.</p>
    </div>

    <svg class="bottom-bands" viewBox="0 0 880 80" preserveAspectRatio="none" aria-hidden="true">
      <polygon points="0,54 565,54 555,80 0,80" fill="#d0111b"/>
      <polygon points="580,30 880,0 880,80 568,80" fill="#050505"/>
    </svg>
  </section>

  <section class="card card-back" aria-label="Business card back">
    <div class="brand">
      <div class="brand-mark" aria-hidden="true"></div>
      <p class="brand-name">Copperfield<br>Roofing Co.</p>
    </div>
  </section>

</body>
</html>
```